Walk Bright through the Seasons: 52 Weeks to a Year of Courage and Calm

This is a non-fiction, self-help book. The first edition was published a decade ago, and it needs a new design. Nothing too literal (no actual hearts on the cover) but something inspirational or perhaps something quite plain. The current cover is below for reference, but I DO NOT want something similar to that. It is outdated.

The cover must include:

1. Title: Walk Bright through the Seasons
2. Subtitle: 52 Weeks to a Year of Courage and Calm
3. Author Name: Tobin Wells

It should also have plenty of "white space" in other words the fonts shouldnt be so big that they take up the whole cover.

Dimensions: 9" x 6.25"

Target Market(s)

adults interested in personal development

Font styles to use
Serif
Script

Colors

Designer to choose colors to be used in the design.

Requirements
Must have
• Classic look and feel. The current design is too busy. I have included examples of the style I like below. I'm open to a singular graphic/photo but nothing more than that. Probably plain text is best.
• Please look at the samples I have included of best-selling books in the genre that I like. The cover should be modeled after these.

```html
<!DOCTYPE html>
<html lang="en">
<head>
<meta charset="utf-8">
<title>Walk Bright through the Seasons — Tobin Wells</title>
<link href="https://fonts.googleapis.com/css2?family=Cormorant+Garamond:wght@400;500;600&family=Pinyon+Script&display=swap" rel="stylesheet">
<style>
  :root {
    --paper: #fbf9f5;
    --ink: #23344a;
    --accent: #4a8fc4;
    --muted: #7b8591;
    --rule: #b9c6d3;
  }
  html, body {
    margin: 0;
    padding: 0;
    width: 841px;
    height: 1200px;
    overflow: hidden;
    background: var(--paper);
  }
  .cover {
    position: relative;
    width: 841px;
    height: 1200px;
    background: var(--paper);
    overflow: hidden;
    font-family: "Cormorant Garamond", serif;
    color: var(--ink);
    text-align: center;
  }
  .frame {
    position: absolute;
    inset: 40px;
    border: 1px solid var(--rule);
  }
  .title {
    position: absolute;
    left: 0;
    right: 0;
    top: 330px;
    margin: 0;
    font-weight: 500;
  }
  .title-main {
    display: block;
    font-size: 68px;
    line-height: 80px;
    letter-spacing: 10px;
    text-transform: uppercase;
  }
  .title-script {
    display: block;
    font-family: "Pinyon Script", cursive;
    font-weight: 400;
    font-size: 56px;
    line-height: 80px;
    color: var(--accent);
    margin: 14px 0 10px;
  }
  .divider {
    position: absolute;
    left: 50%;
    top: 640px;
    width: 200px;
    height: 12px;
    margin-left: -100px;
  }
  .subtitle {
    position: absolute;
    left: 0;
    right: 0;
    top: 690px;
    margin: 0;
    font-weight: 500;
    font-size: 19px;
    letter-spacing: 4px;
    text-transform: uppercase;
    color: var(--muted);
  }
  .author {
    position: absolute;
    left: 0;
    right: 0;
    top: 1030px;
    margin: 0;
    font-weight: 600;
    font-size: 28px;
    letter-spacing: 9px;
    text-transform: uppercase;
    color: var(--ink);
  }
</style>
</head>
<body>
  <main class="cover">
    <div class="frame"></div>
    <h1 class="title">
      <span class="title-main">Walk Bright</span>
      <span class="title-script">through the</span>
      <span class="title-main">Seasons</span>
    </h1>
    <svg class="divider" viewBox="0 0 200 12" aria-hidden="true">
      <line x1="0" y1="6" x2="88" y2="6" stroke="#b9c6d3" stroke-width="1"/>
      <circle cx="100" cy="6" r="3.5" fill="#4a8fc4"/>
      <line x1="112" y1="6" x2="200" y2="6" stroke="#b9c6d3" stroke-width="1"/>
    </svg>
    <p class="subtitle">52 Weeks to a Year of Courage and Calm</p>
    <p class="author">Tobin Wells</p>
  </main>
</body>
</html>
```